Creative - Appealing - Business Card Design Project

Looking for a Business card design (vector artwork) for an existing company called 'Copperfield Sound'. We operate in the entertainment industry specializing in audio system design and rental, however; we also deal with other sectors of the entertainment industry including lighting, video, staging and power system design and rental. We would like to see designs that don't focus too much on audio but include elements encompassing everything else.

Double sided business card, following our new colour scheme and logo, which is attached. The card would ideally be creative and eye catching to draw in new customers in the elegant event production market, such as weddings & corporate affairs.

Target Market(s)

High end corporate clients, wedding clients

Industry/Entity Type

Entertainment

Requirements
Must have
• Our contact details, these can be worded & listed however you think appropriate as part as the design

Business Name - Copperfield Sound
My Name - Benedict Thornbury
Web Address - www.copperfieldsound-example.com
Mobile Number - 07914 362 517
Office Number - 0330 411 7785
Email - ben@copperfieldsound-example.com

The name, email and mobile number would need to be able to be changed to my business partners also.

The font used on our logo is Sansation
Nice to have
• On one side maybe a word cloud involving the services in which we can provide; Lighting, Sound, Event Production, Staging, LED Uplighting, Projection Mapping, Wedding Hire

On the other side, all the important credentials of contact.
Should not have
• The design should not use any old style fonts (i.e Times New Roman, Gothic etc) or on the other side of the scale, any 'jokey' fonts (i.e. Comic Sans).

The font to be used is Sansation

```html
<!DOCTYPE html>
<html lang="en">
<head>
<meta charset="utf-8">
<title>Copperfield Sound – Business Card</title>
<link rel="stylesheet" href="https://fonts.googleapis.com/css2?family=Exo+2:wght@400;500;600&display=swap">
<style>
  :root {
    --backdrop: #e9e1d8;
    --purple-light: #5c3f93;
    --purple-dark: #33205f;
    --purple-ink: #57308c;
    --lavender: #cfc3ee;
    --card-white: #ffffff;
    --text-grey: #7a7a7a;
    --brand-grey: #6e6e6e;
    --shadow: rgba(60, 45, 30, 0.35);
  }
  * { margin: 0; padding: 0; box-sizing: border-box; }
  html, body {
    width: 1200px;
    height: 800px;
    overflow: hidden;
    background: var(--backdrop);
    font-family: "Exo 2", sans-serif;
  }
  .canvas {
    position: relative;
    width: 1200px;
    height: 800px;
  }
  .card {
    position: absolute;
    width: 464px;
    height: 284px;
    border-radius: 20px;
    box-shadow: 3px 4px 8px var(--shadow);
    overflow: hidden;
  }
  /* Brand side */
  .card-brand {
    left: 207px;
    top: 157px;
  }
  .brand-pattern {
    position: absolute;
    inset: 0;
    background: linear-gradient(100deg, var(--purple-light) 0%, #4a2f80 55%, var(--purple-dark) 100%);
  }
  .brand-lockup {
    position: absolute;
    left: 0;
    right: 0;
    top: 78px;
    text-align: center;
    color: var(--lavender);
    font-weight: 600;
  }
  .brand-mark {
    display: block;
    width: 54px;
    height: 54px;
    margin: 0 auto 18px;
    border-radius: 50%;
    background: var(--lavender);
  }
  .brand-name {
    display: block;
    font-size: 22px;
    letter-spacing: 0.5px;
    line-height: 1.1;
    text-transform: uppercase;
  }
  /* Contact side */
  .card-contact {
    left: 565px;
    top: 330px;
    background: var(--card-white);
  }
  .contact-name {
    position: absolute;
    left: 24px;
    top: 34px;
    color: var(--purple-ink);
    font-size: 14.5px;
    font-weight: 600;
    letter-spacing: 0.3px;
    text-transform: uppercase;
  }
  .contact-address {
    position: absolute;
    left: 24px;
    top: 75px;
    color: var(--text-grey);
    font-size: 12px;
    line-height: 24px;
    font-style: normal;
  }
  .contact-list {
    position: absolute;
    left: 24px;
    display: grid;
    grid-template-columns: 52px auto;
    row-gap: 6px;
    color: var(--text-grey);
    font-size: 12px;
    line-height: 18px;
  }
  .contact-list dt, .contact-list dd { margin: 0; }
  .contact-phones { top: 146px; }
  .contact-online { top: 212px; }
  .contact-brand {
    position: absolute;
    left: 300px;
    width: 140px;
    top: 170px;
    text-align: center;
  }
  .contact-brand .mark {
    display: block;
    width: 36px;
    height: 36px;
    margin: 0 auto 20px;
    background: var(--purple-ink);
  }
  .contact-brand .name {
    color: var(--brand-grey);
    font-size: 13px;
    font-weight: 500;
    letter-spacing: 0.3px;
    text-transform: uppercase;
    white-space: nowrap;
  }
</style>
</head>
<body>
<main class="canvas">
  <section class="card card-brand">
    <div class="brand-pattern" role="img" aria-label="Subtle repeating triangle pattern in purple tones"></div>
    <div class="brand-lockup">
      <span class="brand-mark"></span>
      <span class="brand-name">Copperfield Sound</span>
    </div>
  </section>

  <section class="card card-contact">
    <h1 class="contact-name">Benedict Thornbury</h1>
    <address class="contact-address">
      48 Alder Row<br>
      Harwick Park, Eastbourne
    </address>
    <dl class="contact-list contact-phones">
      <dt>Phone</dt><dd>07914 362 517</dd>
      <dt>Mobile</dt><dd>0330 411 7785</dd>
    </dl>
    <dl class="contact-list contact-online">
      <dt>Email</dt><dd>ben@copperfieldsound-example.com</dd>
      <dt>Web</dt><dd>copperfieldsound-example.com</dd>
    </dl>
    <div class="contact-brand">
      <span class="mark"></span>
      <span class="name">Copperfield Sound</span>
    </div>
  </section>
</main>
</body>
</html>
```